Modern and Simple Supplement Label Design

We are looking for a Professional Graphic Designer who can design eye-catching and unique supplement label. We are supplement company who are sourcing different supplement products. I would like the design to be simple and with few colorsThe final design should communicate strength and growthI attached some samples for inspiration

Target Market(s)

Supplement Market - Collagen Supplements

Industry/Entity Type

Supplement

Font styles to use
Serif
Sans Serif

Colors

Designer to choose colors to be used in the design.

Requirements
Must have
• Front (Please search on Amazon Collagen to get inspiration how to put together the front text)
• Logo: Velm Organics
• Product Name: Dorava Blend Capsules
• Hydrolyzed type I II III V & X Collagen
• Dietary Supplements - 90 capsules
• Support Joints & bones
• Rejuvenate Skin
• Promotes Healthy Hair & Nails
• One right side supplement fact and left side precaution and instruction content. ( Please find the content of the right and left side of the bottle attached)
Nice to have
• Nice to have something that shows elements bring together to create something strong or beautiful. Our brand name is Velm Organics. Velm is an assembly of beams or other elements that creates a rigid structure. This is to show our supplements help to provide the elements to have strong and healthy life

```html
<!DOCTYPE html>
<html lang="en">
<head>
<meta charset="utf-8">
<title>Velm Organics – Dorava Blend Capsules Label</title>
<link href="https://fonts.googleapis.com/css2?family=Archivo+Narrow:wght@700&family=Roboto+Condensed:wght@400;500;700&family=Open+Sans:wght@400;600&display=swap" rel="stylesheet">
<style>
  :root {
    --navy: #0f1f3d;
    --orange-deep: #c2641a;
    --orange-light: #eba53a;
    --label-white: #f7f8f8;
    --label-grey: #e3e6e7;
    --ink: #141414;
    --backdrop: #dfe5e6;
  }
  * { margin: 0; padding: 0; box-sizing: border-box; }
  html, body { width: 1200px; height: 901px; overflow: hidden; }
  body {
    background: var(--backdrop);
    font-family: "Open Sans", Arial, sans-serif;
    color: var(--ink);
    position: relative;
  }
  .label {
    position: absolute;
    left: 40px; top: 170px;
    width: 1120px; height: 560px;
    box-shadow: 0 6px 24px rgba(0,0,0,.12);
    overflow: hidden;
  }
  .label-shapes { position: absolute; inset: 0; }
  .side-panel {
    position: absolute;
    top: 40px;
    width: 240px;
    font-family: "Roboto Condensed", Arial, sans-serif;
    font-size: 14px;
    line-height: 1.4;
    color: var(--ink);
  }
  .side-panel--left { left: 32px; }
  .side-panel--right { left: 850px; }
  .side-heading {
    font-weight: 700;
    font-size: 16px;
    text-transform: uppercase;
    margin: 14px 0 4px;
  }
  .side-heading:first-child { margin-top: 0; }
  .facts {
    border: 2px solid var(--ink);
    padding: 8px 10px;
    background: #fff;
  }
  .facts-title {
    font-family: "Archivo Narrow", Arial, sans-serif;
    font-size: 28px;
    line-height: 1;
    border-bottom: 1px solid var(--ink);
    padding-bottom: 6px;
    margin-bottom: 6px;
  }
  .facts-row { display: flex; justify-content: space-between; }
  .facts-rule-thick { border-bottom: 6px solid var(--ink); margin: 6px 0; }
  .facts-rule { border-bottom: 1px solid var(--ink); margin: 4px 0; }
  .facts-head { font-weight: 700; }
  .facts-note { font-size: 12px; margin-top: 6px; }
  .other-ingredients { margin-top: 10px; font-size: 13px; }

  .brand {
    position: absolute;
    left: 400px; top: 26px;
    width: 320px;
    display: flex; align-items: center; justify-content: center; gap: 10px;
    font-family: "Roboto Condensed", Arial, sans-serif;
    font-weight: 500;
    font-size: 28px;
    color: #fff;
  }
  .brand-mark {
    width: 26px; height: 26px;
    border: 3px solid #fff;
  }
  .product-name {
    position: absolute;
    left: 300px; top: 124px;
    width: 520px;
    text-align: center;
    font-family: "Archivo Narrow", Arial, sans-serif;
    font-weight: 700;
    font-size: 56px;
    line-height: 1.02;
    letter-spacing: .5px;
    color: var(--ink);
  }
  .product-type {
    position: absolute;
    left: 300px; top: 252px;
    width: 520px;
    text-align: center;
    font-family: "Roboto Condensed", Arial, sans-serif;
    font-weight: 700;
    font-size: 22px;
    color: var(--ink);
  }
  .benefits {
    position: absolute;
    left: 395px; top: 307px;
    width: 330px;
    list-style: none;
    text-align: center;
    font-family: "Roboto Condensed", Arial, sans-serif;
    font-size: 21px;
    line-height: 1.28;
    color: #fff;
  }
  .dietary {
    position: absolute;
    left: 300px; top: 446px;
    width: 520px;
    text-align: center;
    font-size: 15px;
    color: var(--ink);
  }
  .count {
    position: absolute;
    left: 300px; top: 470px;
    width: 520px;
    display: flex; align-items: center; justify-content: center; gap: 8px;
    font-family: "Open Sans", Arial, sans-serif;
    font-weight: 600;
    font-size: 24px;
    letter-spacing: 2px;
    color: var(--ink);
  }
  .count-number {
    width: 42px; height: 42px;
    border-radius: 50%;
    background: var(--navy);
    color: #fff;
    display: flex; align-items: center; justify-content: center;
    letter-spacing: 0;
    font-size: 22px;
  }
</style>
</head>
<body>
  <section class="label">
    <svg class="label-shapes" width="1120" height="560" viewBox="0 0 1120 560">
      <defs>
        <linearGradient id="labelBase" x1="0" y1="0" x2="0" y2="1">
          <stop offset="0" stop-color="var(--label-white)"/>
          <stop offset="1" stop-color="var(--label-grey)"/>
        </linearGradient>
        <linearGradient id="accentBand" x1="0" y1="0" x2="1" y2="1">
          <stop offset="0" stop-color="var(--orange-light)" stop-opacity=".55"/>
          <stop offset=".45" stop-color="var(--orange-deep)"/>
          <stop offset="1" stop-color="var(--orange-light)" stop-opacity=".7"/>
        </linearGradient>
      </defs>
      <rect class="label-base" width="1120" height="560" fill="url(#labelBase)"/>
      <polygon class="accent-band" role="img" aria-label="Orange diagonal band of small assembled triangles"
               points="300,60 420,60 820,470 820,560 300,560" fill="url(#accentBand)"/>
      <polygon class="brand-banner" points="400,0 720,0 720,78 560,110 400,78" fill="var(--navy)"/>
      <polygon class="benefit-plate" points="418,300 702,300 725,360 702,420 418,420 395,360" fill="var(--navy)"/>
    </svg>

    <div class="side-panel side-panel--left">
      <p class="side-heading">Directions</p>
      <p>Take three capsules daily with water, or as directed by your healthcare professional.</p>
      <p class="side-heading">Caution</p>
      <p>Consult your physician before use if you are pregnant, nursing, taking medication or have a medical condition.</p>
      <p>Keep out of reach of children. Store in a cool, dry place.</p>
      <p>Do not use if seal is broken or missing.</p>
    </div>

    <div class="brand"><span class="brand-mark"></span>Velm Organics</div>
    <h1 class="product-name">Dorava Blend<br>Capsules</h1>
    <p class="product-type">Hydrolyzed type I II III V &amp; X Collagen</p>
    <ul class="benefits">
      <li>Support Joints &amp; bones</li>
      <li>Rejuvenate Skin</li>
      <li>Promotes Healthy Hair &amp; Nails</li>
    </ul>
    <p class="dietary">Dietary Supplements</p>
    <p class="count"><span class="count-number">90</span>Capsules</p>

    <div class="side-panel side-panel--right">
      <div class="facts">
        <h2 class="facts-title">Supplement Facts</h2>
        <p>Serving Size 3 Capsules</p>
        <p>Servings Per Container 30</p>
        <div class="facts-rule-thick"></div>
        <div class="facts-row facts-head"><span>Amount Per Serving</span><span>% DV</span></div>
        <div class="facts-rule"></div>
        <div class="facts-row"><span>Hydrolyzed Collagen Blend</span><span>1500 mg †</span></div>
        <div class="facts-rule-thick"></div>
        <p class="facts-note">† Daily Value not established.</p>
      </div>
      <p class="other-ingredients">Other ingredients: gelatin capsule, rice flour.</p>
    </div>
  </section>
</body>
</html>
```